Brightline Servicing-work at height professionals

Specializing In:
High Rise Window Washing
Interior atrium maintenance
Dryer vent cleaning
Building maintenance/inspection
Property maintenance
Pressure washing

Portray:experienced team, QLVOM certified technicians,

Needs to portray the rope access industry and window washing via rope access (not bosun chair!)

Pictures are just examples only of our work
Updates

Designs are looking good! Check the brief again. I updated it

Please change “hi-rise to”High Rise” Thanks, and check rest of the brief for updates on spelling and wording Thanks, designs are looking good!

Aswell need a company logo with the designs Thanks

Target Market(s)

High rise property management companies

Industry/Entity Type

Property Maintenance

Contact Information for Business Card

Torren Mabry
Brightline Servicing
Work at height professionals
C:555-302-7816
E:torren@brightlineservicing.co
E:sales@brightlineservicing.co
Serving southern Alberta

Font styles to use
Sans Serif

Colors

Designer to choose colors to be used in the design.

Requirements
Must have
• High Rise Window Washing
• Dryer Vent Cleaning
• Snow Management
• Interior Atriums Maintenance
• Property Maintenance
• QLVOM Certified
Nice to have
• Work at Height Professionals
• For all your property maintenance needs
• A company logo
• Downtown Calgary Alberta background
Should not have
• Bosun chairs
• Hi-rise

```html
<!DOCTYPE html>
<html lang="en">
<head>
<meta charset="utf-8">
<title>Brightline Servicing – Business Cards</title>
<link rel="stylesheet" href="https://fonts.googleapis.com/css2?family=Open+Sans:wght@400;600;700&display=swap">
<style>
  :root {
    --bg: #2a2a2b;
    --card-dark: #2d2e30;
    --gold: #c2b336;
    --gold-light: #d6ca4f;
    --gold-deep: #a8962a;
    --ink: #111111;
    --white: #f4f4f2;
  }
  * { margin: 0; padding: 0; box-sizing: border-box; }
  html, body { width: 1200px; height: 800px; overflow: hidden; }
  body {
    background: var(--bg);
    font-family: "Open Sans", Arial, sans-serif;
    position: relative;
  }
  .card {
    position: absolute;
    top: 245px;
    width: 540px;
    height: 310px;
    overflow: hidden;
  }
  .card svg.card-shapes { position: absolute; inset: 0; }
  .card-back { left: 40px; }
  .card-front { left: 620px; }

  /* Back card */
  .company-title {
    position: absolute; left: 22px; top: 34px;
    color: var(--gold);
    font-weight: 700; font-size: 30px; line-height: 31px;
  }
  .services-heading {
    position: absolute; left: 24px; top: 132px;
    color: var(--gold); font-weight: 600; font-size: 16px;
  }
  .services-list {
    position: absolute; left: 24px; top: 158px;
    list-style: none; color: var(--white);
    font-size: 11.5px; line-height: 16.5px;
  }
  .services-list li::before {
    content: ""; display: inline-block;
    width: 5px; height: 5px; background: var(--gold);
    margin-right: 6px; vertical-align: middle;
  }

  /* Front card */
  .person-name {
    position: absolute; left: 30px; top: 30px;
    font-weight: 700; font-size: 27px; color: var(--ink);
    text-transform: uppercase; letter-spacing: -0.3px;
  }
  .person-role {
    position: absolute; left: 30px; top: 64px;
    font-size: 15px; color: var(--white);
  }
  .contact-list {
    position: absolute; right: 30px; top: 100px;
    list-style: none;
    color: var(--white); font-size: 14.5px;
  }
  .contact-list li {
    height: 42px;
    display: flex; justify-content: flex-end; align-items: center; gap: 6px;
  }
  .contact-list .value { line-height: 20px; white-space: nowrap; }
  .contact-list svg.icon { flex: none; align-self: flex-end; margin-bottom: 8px; }
  .brand-mark {
    position: absolute; left: 22px; top: 228px;
    display: flex; align-items: center; gap: 8px;
  }
  .brand-mark .mark-square {
    width: 18px; height: 18px; border: 3px solid var(--white);
  }
  .brand-mark .brand-name {
    color: var(--white); font-weight: 700; font-size: 19px; letter-spacing: 0.5px;
    text-transform: uppercase;
  }
</style>
</head>
<body>

<section class="card card-back">
  <svg class="card-shapes" width="540" height="310" viewBox="0 0 540 310">
    <defs>
      <linearGradient id="backDark" x1="0" y1="0" x2="1" y2="1">
        <stop offset="0" stop-color="#363739"/>
        <stop offset="1" stop-color="#252628"/>
      </linearGradient>
      <linearGradient id="cityTone" x1="0" y1="0" x2="0" y2="1">
        <stop offset="0" stop-color="#c9d6e2"/>
        <stop offset="0.55" stop-color="#a9b4c0"/>
        <stop offset="1" stop-color="#eef1f4"/>
      </linearGradient>
    </defs>
    <rect width="540" height="310" fill="url(#backDark)"/>
    <line x1="18" y1="100" x2="275" y2="100" stroke="#c2b336" stroke-width="1.5"/>
    <polygon points="270,20 310,20 310,0 540,0 540,270 250,270 250,150" fill="#c2b336"/>
    <g role="img" aria-label="Photo of a snowy downtown skyline">
      <polygon points="282,30 325,30 325,12 528,12 528,258 262,258 262,160" fill="url(#cityTone)"/>
    </g>
  </svg>
  <h1 class="company-title">Brightline<br>Servicing</h1>
  <h2 class="services-heading">Company specializes in:</h2>
  <ul class="services-list">
    <li>Rope access operations</li>
    <li>High Rise window washing</li>
    <li>Interior atriums maintenance</li>
    <li>Dryer vent cleaning</li>
    <li>Snow management</li>
    <li>Property maintenance</li>
    <li>Experienced and reliable</li>
    <li>Have QLVOM certified technicians</li>
  </ul>
</section>

<section class="card card-front">
  <svg class="card-shapes" width="540" height="310" viewBox="0 0 540 310">
    <defs>
      <linearGradient id="goldPanel" x1="0" y1="1" x2="1" y2="0">
        <stop offset="0" stop-color="#a8962a"/>
        <stop offset="0.5" stop-color="#c2b336"/>
        <stop offset="1" stop-color="#d6ca4f"/>
      </linearGradient>
    </defs>
    <rect width="540" height="310" fill="#2d2e30"/>
    <polygon points="0,10 225,10 240,28 540,28 540,310 200,310 185,288 0,288" fill="url(#goldPanel)"/>
    <g fill="#2d2e30">
      <rect x="512" y="98" width="5" height="38"/>
      <rect x="512" y="140" width="5" height="38"/>
      <rect x="512" y="182" width="5" height="38"/>
      <rect x="512" y="224" width="5" height="38"/>
    </g>
  </svg>
  <h2 class="person-name">Torren Mabry</h2>
  <p class="person-role">Executive Officer</p>
  <ul class="contact-list">
    <li>
      <span class="value">555-302-7816</span>
      <svg class="icon" width="10" height="10" viewBox="0 0 24 24"><path fill="#2d2e30" d="M6.6 10.8a15 15 0 0 0 6.6 6.6l2.2-2.2a1 1 0 0 1 1-.25 11.4 11.4 0 0 0 3.6.57 1 1 0 0 1 1 1V20a1 1 0 0 1-1 1A17 17 0 0 1 3 4a1 1 0 0 1 1-1h3.5a1 1 0 0 1 1 1c0 1.25.2 2.45.57 3.57a1 1 0 0 1-.25 1z"/></svg>
    </li>
    <li>
      <span class="value">torren@brightlineservicing.co</span>
      <svg class="icon" width="11" height="9" viewBox="0 0 22 16"><rect x="1" y="1" width="20" height="14" fill="none" stroke="#2d2e30" stroke-width="2"/><path d="M1 1l10 8 10-8" fill="none" stroke="#2d2e30" stroke-width="2"/></svg>
    </li>
    <li>
      <span class="value">sales@brightlineservicing.co</span>
      <svg class="icon" width="11" height="11" viewBox="0 0 24 24"><circle cx="12" cy="12" r="10" fill="none" stroke="#2d2e30" stroke-width="2"/><ellipse cx="12" cy="12" rx="4" ry="10" fill="none" stroke="#2d2e30" stroke-width="2"/><line x1="2" y1="12" x2="22" y2="12" stroke="#2d2e30" stroke-width="2"/></svg>
    </li>
    <li>
      <span class="value">Serving southern Alberta</span>
      <svg class="icon" width="11" height="10" viewBox="0 0 24 22"><path fill="#2d2e30" d="M12 1 1 11h3v10h6v-6h4v6h6V11h3z"/></svg>
    </li>
  </ul>
  <div class="brand-mark">
    <span class="mark-square"></span>
    <span class="brand-name">Brightline Servicing</span>
  </div>
</section>

</body>
</html>
```